【表紙要素】

■書籍タイトル
頼りない課長だった僕が十五期続いた欠損の倉庫業者を再生させた方法

■サブタイトル
町工場のための統率術入門

■キャッチコピー1
「灯台守ステップ術」で部下はあなたについてくる

■キャッチコピー2
特別セミナー動画(無料プレゼント)付き
「粗利が倍増する。倉庫業者が今日から使える5つの収益改善フレーム」

■著者
桐島のぶお

■肩書
物流マーケティングコンサルタント
次世代リーダー育成コンサルタント

■書籍の内容
総合物流会社から赤字続きの関連小会社へ出向となった著者が、会社を立て直す中で学んだリーダーシップ論がテーマになっています。原稿も添付いたします。

■ターゲット
運輸会社の経営者・部課長をターゲットとしています。

■デザイン要望
・イラストを入れるとすると、売上が右肩上がりになっているグラフなどのイメージかなと思いってます。もちろん、その他に良いアイデアがあれば採用したいと思います。
・イラストが入っても、文字だけでも、どちらでも構いません。できれば両方のパターンを比較して決めたいと思います。
・タイトルに関しては、「頼りない課長だった僕が」は小さく、「赤字」「黒字化」は目立つようにお願いします。

本の本文の内容が、あまり堅苦しくない、おもしろおかしい要素が含まれていますので、表紙も明るくてポップな感じが気に入りました。
ただし、誠に申し訳ないのですが、急遽、電子書籍のタイトルを変更することになりました。また、表紙の文字数も減らすことにしました。
したがいまして、今回のコンペとは別に、本日中に再発注をかけます。
何卒、ご理解いただき、再度コンペへのご参加をお願いいたします。

ご提案いただき、ありがとうございました。また、原稿を読んで頂き、内容を踏まえた上でデザインを考えていただき、大変感謝しています。
いろいろと考えた結果、急遽、電子書籍のタイトルを変更することになりました。今回のコンペとは別に、再度依頼をかけますので、またコンペにご参加いただけますようお願いいたします。

```html
<!DOCTYPE html>
<html lang="ja">
<head>
<meta charset="utf-8">
<title>頼りない課長だった僕が十五期続いた欠損の倉庫業者を再生させた方法</title>
<link href="https://fonts.googleapis.com/css2?family=Noto+Sans+JP:wght@500;700;900&display=swap" rel="stylesheet">
<style>
  :root{
    --ink:#1b1b1b;
    --red:#e5231d;
    --paper:#ffffff;
    --road-light:#e6e6e6;
  }
  *{margin:0;padding:0;box-sizing:border-box}
  html,body{width:753px;height:1200px;overflow:hidden;background:var(--paper)}
  .cover{position:relative;width:753px;height:1200px;overflow:hidden;background:var(--paper);
    font-family:"Noto Sans JP",sans-serif;color:var(--ink)}
  .vertical{position:absolute;writing-mode:vertical-rl;text-orientation:upright;line-height:1;white-space:nowrap}

  .road-art{position:absolute;left:140px;top:610px;width:470px;height:260px;z-index:0;
    background:radial-gradient(ellipse at 50% 0%, var(--road-light) 0%, #c4c4c4 45%, rgba(255,255,255,0) 72%);}
  .growth-arrow{position:absolute;left:266px;top:360px;width:220px;height:500px;z-index:1}

  .title-lead{right:40px;top:22px;font-size:38px;font-weight:700;letter-spacing:2px}
  .title-line{font-weight:900;font-size:64px;letter-spacing:-1px}
  .title-line.first{right:110px;top:24px}
  .title-line.second{right:205px;top:24px}
  .title-line.third{right:300px;top:24px}
  .accent-red{color:var(--red)}
  .accent-box{display:inline-block;background:var(--ink);color:var(--paper);padding:8px 6px;margin:6px 0}

  .subtitle{left:188px;top:40px;font-size:38px;font-weight:900;letter-spacing:3px}
  .subtitle::before{content:"";position:absolute;left:-14px;top:0;height:100%;border-left:2px solid var(--ink)}

  .author{position:absolute;left:62px;top:722px;z-index:2;line-height:1.3;white-space:nowrap}
  .author-role{font-size:17px;font-weight:700}
  .author-name{font-size:40px;font-weight:900;margin-top:4px;letter-spacing:1px;line-height:1.15}
  .author-roman{font-size:13px;font-weight:500}

  .bonus{position:absolute;right:14px;top:745px;width:150px;text-align:center;z-index:2}
  .bonus svg{display:block;margin:0 auto 8px}
  .bonus-label{background:var(--ink);color:var(--paper);border-radius:14px;padding:12px 4px;
    font-size:21px;font-weight:900;line-height:1.25;white-space:nowrap}
  .bonus-label small{display:block;font-size:13px;font-weight:700}

  .pitch{position:absolute;left:60px;top:870px;z-index:2;white-space:nowrap}
  .method{display:inline-block;background:var(--paper);border:2px solid var(--ink);padding:2px 10px;font-size:26px;font-weight:900}
  .method-follow{font-size:28px;font-weight:900;margin:4px 0 0 10px;line-height:1.3}
  .headline{position:absolute;left:60px;top:966px;z-index:2;font-size:64px;font-weight:900;line-height:1.2;color:var(--red);letter-spacing:-1px;white-space:nowrap}
  .offer{position:absolute;left:60px;top:1050px;z-index:2;font-size:50px;font-weight:900;line-height:1.2;white-space:nowrap}
</style>
</head>
<body>
<main class="cover">
  <div class="road-art" role="img" aria-label="地平線へ向かって伸びる灰色の道路のイラスト"></div>
  <svg class="growth-arrow" viewBox="0 0 220 500" aria-hidden="true">
    <defs>
      <linearGradient id="arrowFade" x1="0" y1="1" x2="0" y2="0">
        <stop offset="0" stop-color="#e5231d" stop-opacity="0"/>
        <stop offset="0.45" stop-color="#e5231d"/>
        <stop offset="1" stop-color="#e5231d"/>
      </linearGradient>
    </defs>
    <polygon points="110,0 220,110 150,110 150,500 70,500 70,110 0,110" fill="url(#arrowFade)"/>
  </svg>

  <p class="vertical title-lead">頼りない課長だった僕が</p>
  <h1>
    <span class="vertical title-line first">十五期続いた<span class="accent-red">欠損</span>の</span>
    <span class="vertical title-line second">倉庫業者を<span class="accent-box">再生</span></span>
    <span class="vertical title-line third">させた方法</span>
  </h1>
  <p class="vertical subtitle">町工場のための統率術入門</p>

  <div class="author">
    <p class="author-role">物流マーケティングコンサルタント</p>
    <p class="author-role">次世代リーダー育成コンサルタント</p>
    <p class="author-name">桐島のぶお</p>
    <p class="author-roman">Nobuo Kirishima</p>
  </div>

  <div class="bonus">
    <svg width="110" height="80" viewBox="0 0 110 80" aria-hidden="true">
      <rect x="4" y="6" width="66" height="50" rx="4" fill="#1b1b1b"/>
      <path d="M72 22h20l14 16v18H72z" fill="#1b1b1b"/>
      <rect x="78" y="27" width="12" height="10" fill="#fff"/>
      <circle cx="24" cy="62" r="10" fill="#1b1b1b" stroke="#fff" stroke-width="3"/>
      <circle cx="88" cy="62" r="10" fill="#1b1b1b" stroke="#fff" stroke-width="3"/>
    </svg>
    <p class="bonus-label">特別<br>セミナー動画<small>(無料プレゼント)</small>付き</p>
  </div>

  <div class="pitch">
    <p class="method">「灯台守ステップ術」で</p>
    <p class="method-follow">部下はあなたについてくる</p>
  </div>
  <p class="headline">粗利が倍増する！</p>
  <p class="offer">倉庫業者が今日から使える<br>5つの収益改善フレーム</p>
</main>
</body>
</html>
```